Professional Document Wallet Design - Corporate Presentation Folder Design

Corporate Presentation Folder is known as a Document Wallet in Ireland.

This listing is for a design of a product called 'Document Wallets' - design for both inside and out. An example of the finished product is attached - 'preview document wallet.png'. This gives a clear example of what the document wallet looks like and for further details about this product you can visit this link.
http://www.presswerk-example.com/ie/group/double-gloss-lam-interlocking-presentation-folders
Attached "finish-image-1.jpg" gives an overview of the product outline as well as dimensions - also "preview document wallet"

'P10 template.indd' or 'P10 template.pdf' give the most detailed measurements of the product as these are the actual templates to be used in printing the product and therefore designs must be delivered on either of these.

Company Background

The client is a professional construction group and leads some of the largest construction jobs in the country for clients such as norvex, brado and tellura to name a few.
The brief is to design a document wallet both sides that reflects well on their corporate clients, shows off their existing branding clearly and highlights their strengths completely.
The clients current branding can be seen at this address http://dunphy.vantrelmedia.example/ but please be aware this website is still a work in progress.
An example of stationery styling liked by the client is found in the attached, Example of styling.pdf

Contents of the Design

As these document are a touch point for the company it is imperative that the following information is included.

1. The Company Logo
This must be clearly visible and the colouring around it enhance it's visibility. The logo should be to the fore and the design in no way should distract or detract attention from it.
2. Company Address and other contact details.
Address
Fernmount,
Kilcorrib,
Castlerea,
Co. Roscommon

T: 094 9270446
E: info@dunphygroup.example
W: www.dunphygroup.example

3. Some images should be included and can be found at
https://files.storebox.example/folderview?id=0X_QTrPmWjLsNnR7KdQ2bHcUeFa&usp=sharing
but stock images can be used if required to ensure the most professional look and feel for the project.

Printing
UV spot printing will be used on this printing and it is a requirement of the design to incorporate this into the finished article in some way. The document wallets are double sided so the same design should run throughout and consideration given to the user opening the wallet.
Updates

Target Market(s)

Professional corporate Clients

Industry/Entity Type

Product

Requirements
Must have
• Professional
• Striking
• Branding
• Logo
• Contact details
Nice to have
• A design surrounding the business card holder o the document wallet to enhance the area where the business card is held.

```html
<!DOCTYPE html>
<html lang="en">
<head>
<meta charset="utf-8">
<title>Dunphy Group – Document Wallet, Inside Spread</title>
<link rel="stylesheet" href="https://fonts.googleapis.com/css2?family=Montserrat:wght@400;600;700&display=swap">
<style>
  :root {
    --backdrop: #2b2a8c;
    --wallet-black: #060606;
    --pocket-black: #141414;
    --pocket-pattern: #2a2a2a;
    --mark-white: #e9e9e9;
    --card-white: #ffffff;
    --brand-violet: #3b3497;
    --card-ink: #4a4a55;
  }
  * { box-sizing: border-box; margin: 0; padding: 0; }
  html, body { width: 1200px; height: 847px; overflow: hidden; }
  body {
    background: var(--backdrop);
    font-family: "Montserrat", Arial, sans-serif;
    position: relative;
  }
  .wallet {
    position: absolute;
    left: 130px;
    top: 100px;
    width: 940px;
    height: 647px;
    display: flex;
    gap: 4px;
  }
  .wallet-panel {
    position: relative;
    flex: 1;
    background: var(--wallet-black);
    overflow: hidden;
  }
  .pocket {
    position: absolute;
    left: 0;
    right: 0;
    bottom: 0;
    height: 230px;
    border-top: 1px solid #333;
    background:
      repeating-linear-gradient(45deg, var(--pocket-black) 0 14px, var(--pocket-pattern) 14px 16px),
      var(--pocket-black);
  }
  .brand-mark {
    position: absolute;
    left: 190px;
    top: 245px;
    display: flex;
    align-items: center;
    gap: 8px;
  }
  .brand-mark .square {
    width: 34px;
    height: 34px;
    background: var(--mark-white);
  }
  .brand-mark .name {
    color: var(--mark-white);
    font-weight: 600;
    font-size: 20px;
    letter-spacing: 0.5px;
  }
  .business-card {
    position: absolute;
    left: 130px;
    top: 78px;
    width: 190px;
    height: 108px;
    background: var(--card-white);
    border-top: 4px solid var(--brand-violet);
    border-bottom: 4px solid var(--brand-violet);
    padding: 10px 14px;
    box-shadow: 0 2px 6px rgba(0,0,0,0.5);
  }
  .card-brand {
    display: flex;
    align-items: center;
    gap: 5px;
  }
  .card-brand .square {
    width: 16px;
    height: 16px;
    background: var(--brand-violet);
  }
  .card-brand .name {
    color: var(--brand-violet);
    font-weight: 700;
    font-size: 12px;
    line-height: 1;
  }
  .card-brand .sub {
    display: block;
    font-weight: 400;
    font-size: 6px;
    color: var(--card-ink);
    margin-top: 2px;
  }
  .card-details {
    margin-top: 16px;
    text-align: center;
    font-size: 5.5px;
    line-height: 1.45;
    color: var(--card-ink);
    font-style: normal;
  }
</style>
</head>
<body>
  <main class="wallet">
    <section class="wallet-panel wallet-panel--left">
      <div class="brand-mark">
        <span class="square"></span>
        <span class="name">Dunphy</span>
      </div>
      <div class="pocket" role="img" aria-label="Spot UV pattern of repeated brand mark across the pocket"></div>
    </section>
    <section class="wallet-panel wallet-panel--right">
      <div class="pocket" role="img" aria-label="Spot UV pattern of repeated brand mark across the pocket">
        <div class="business-card">
          <div class="card-brand">
            <span class="square"></span>
            <span class="name">Dunphy<span class="sub">Group</span></span>
          </div>
          <address class="card-details">
            1480 Harrowgate Rd, Suite 12<br>
            Lindell Bay, MI 40117<br>
            Tel: 248 555 0142<br>
            www.dunphygroup.example
          </address>
        </div>
      </div>
    </section>
  </main>
</body>
</html>
```